Out of town New Masters of Accounting

size of ad is 7” x 9.6”
please leave one inch on bottom for footer
We want to attract out of town students to join this master's in accounting program.
You DO NOT  have to use a picture of a person.
But if you do, it should be a  male with a white shirt and should not have long hair.(look like a young executive)
THE TEXT OF THE AD IS IN THE ATTACHMENTS
THE CAP LETTERS ARE THE INSTRUCTIONS

The age we are trying to attract is from 20-30 of ages.
- a clear ad .. the text should not take up the entire ad.. it should not be very crowded -
it should be an attractive ad that people would want to see and stand out
- the text very big and take up the entire ad

```html
<!DOCTYPE html>
<html lang="en">
<head>
<meta charset="utf-8">
<title>Out of Town Master's in Accounting – Ad Variations</title>
<link href="https://fonts.googleapis.com/css2?family=Montserrat:wght@500;600;700;800;900&family=Oswald:wght@500;600&family=Source+Sans+3:wght@400&display=swap" rel="stylesheet">
<style>
  :root {
    --sheet: #e6e3e1;
    --cyan: #16a9ea;
    --band-dark: #0b66b2;
    --band-light: #17a8e8;
    --navy: #0d4f96;
    --yellow: #ffd200;
    --ink: #1a1a1a;
    --white: #ffffff;
    --footer-black: #0c0c0c;
    --badge: #f39a1e;
  }
  * { margin: 0; padding: 0; box-sizing: border-box; }
  html, body { width: 1200px; height: 550px; overflow: hidden; background: var(--sheet); }
  .sheet { position: relative; width: 1200px; height: 550px; font-family: "Montserrat", sans-serif; }
  .sheet-title {
    position: absolute; left: 326px; top: 3px;
    font-family: "Source Sans 3", sans-serif; font-size: 19px; color: var(--ink);
  }
  .flyer { position: absolute; top: 35px; width: 350px; height: 480px; background: var(--white); overflow: hidden; }
  .flyer--a { left: 25px; }
  .flyer--b { left: 426px; }
  .flyer--c { left: 823px; }

  .hero-photo { position: absolute; left: 0; top: 0; width: 350px; height: 232px; }
  .flyer--a .hero-photo { background: linear-gradient(160deg, #5a4432 0%, #3b2f27 45%, #2a2a2e 100%); }
  .flyer--b .hero-photo { background: linear-gradient(160deg, #2f3847 0%, #3c4859 50%, #27303d 100%); }
  .flyer--c .hero-photo { background: linear-gradient(160deg, #2e3436 0%, #3f484b 50%, #2a3032 100%); }

  .lead { position: absolute; left: 0; width: 350px; top: 30px; text-align: center; color: var(--white); font-weight: 700; font-size: 13px; }
  .headline {
    position: absolute; left: 0; width: 350px; top: 51px; text-align: center;
    color: var(--cyan); font-weight: 900; font-size: 32px; line-height: 34px; letter-spacing: -0.3px;
  }
  .since { position: absolute; left: 0; width: 350px; top: 155px; text-align: center; color: var(--white); font-weight: 700; font-size: 13px; }
  .duration { position: absolute; left: 0; width: 350px; top: 176px; text-align: center; color: var(--yellow); font-weight: 800; font-size: 13.5px; }
  .swoosh { position: absolute; left: 145px; top: 198px; width: 160px; height: 22px; }

  .promo-band { position: absolute; left: 0; top: 222px; width: 350px; height: 70px; }
  .promo-new {
    position: absolute; left: 11px; top: 242px; font-family: "Oswald", sans-serif; font-weight: 600;
    font-size: 31px; line-height: 36px; color: var(--yellow);
  }
  .promo-remote {
    position: absolute; left: 84px; top: 240px; color: var(--white); font-weight: 800;
    font-size: 12.5px; line-height: 14px;
  }
  .promo-date { position: absolute; left: 224px; top: 229px; width: 126px; text-align: center; color: var(--white); }
  .promo-date .begin { font-size: 10px; font-weight: 800; line-height: 13px; }
  .promo-date .date { font-size: 19px; font-weight: 900; line-height: 20px; }
  .promo-date .price { font-size: 9.5px; font-weight: 800; color: var(--navy); line-height: 14px; }

  .advantage-title { position: absolute; left: 27px; top: 302px; color: var(--cyan); font-weight: 700; font-size: 11.5px; }
  .advantage-list { position: absolute; left: 27px; top: 319px; list-style: none; }
  .advantage-list li { display: flex; align-items: center; gap: 5px; height: 20px; font-size: 10.5px; font-weight: 500; color: var(--ink); }
  .advantage-list svg { width: 10px; height: 10px; flex: none; }

  .program-box {
    position: absolute; left: 27px; top: 381px; width: 196px; height: 39px;
    border: 2px solid var(--navy); border-radius: 14px; text-align: center; padding-top: 7px;
    font-size: 9.5px; line-height: 11.5px; color: var(--ink);
  }
  .program-box strong { font-weight: 700; }
  .ranking-badge { position: absolute; left: 245px; top: 340px; width: 72px; height: 72px; border-radius: 50%; background: var(--badge); }

  .footer { position: absolute; left: 0; top: 430px; width: 350px; height: 50px; }
  .footer-shape { position: absolute; left: 0; top: 0; width: 350px; height: 50px; }
  .org-name { position: absolute; left: 13px; top: 10px; width: 140px; color: var(--white); font-weight: 700; font-size: 10px; line-height: 11px; }
  .org-parent {
    position: absolute; left: 13px; top: 34px; background: var(--footer-black); color: var(--white);
    font-size: 5.8px; font-weight: 500; padding: 1px 3px; white-space: nowrap;
  }
  .contact { position: absolute; left: 156px; top: 11px; width: 142px; color: var(--white); font-size: 5.6px; font-weight: 600; line-height: 10.5px; list-style: none; }
  .contact li { display: flex; align-items: center; gap: 3px; white-space: nowrap; }
  .contact .address { font-weight: 500; }
  .contact svg { width: 6px; height: 6px; flex: none; }
  .audience {
    position: absolute; left: 303px; top: 3px; width: 41px; height: 42px; background: var(--band-light); border-radius: 4px;
    color: var(--white); font-family: "Oswald", sans-serif; font-weight: 500; font-size: 12px; line-height: 14px; text-align: center; padding-top: 6px;
  }
</style>
</head>
<body>
<div class="sheet">
  <p class="sheet-title">Three Different Images</p>

  <!-- Variation A -->
  <article class="flyer flyer--a">
    <div class="hero-photo" role="img" aria-label="Photo of an accountant's desk with calculator, charts, glasses and keyboard, darkened"></div>
    <p class="lead">Advance your career with a</p>
    <h1 class="headline">MASTERS OF<br>SCIENCE IN<br>ACCOUNTING</h1>
    <p class="since">Since 2005</p>
    <p class="duration">Master’s in only 15 months</p>
    <svg class="swoosh" viewBox="0 0 160 22"><path d="M2 18 C40 2 110 0 158 4 C110 4 50 10 10 22 Z" fill="#ffd200"/></svg>
    <svg class="promo-band" viewBox="0 0 350 70"><polygon points="0,5 240,5 262,69 0,69" fill="#0b66b2"/><polygon points="238,2 350,2 350,59 213,59" fill="#17a8e8"/></svg>
    <p class="promo-new">NEW!</p>
    <p class="promo-remote">REMOTE PROGRAM<br>FOR OUT OF TOWN<br>STUDENTS</p>
    <div class="promo-date"><p class="begin">BEGINNING</p><p class="date">AUGUST 17</p><p class="price">NEW LOWER PRICES</p></div>
    <h2 class="advantage-title">Northgate Job Placement Advantage</h2>
    <ul class="advantage-list">
      <li><svg viewBox="0 0 10 10"><circle cx="5" cy="5" r="4.3" fill="none" stroke="#0b66b2" stroke-width="1.2"/><path d="M3 5.2 4.5 6.6 7.2 3.6" fill="none" stroke="#0b66b2" stroke-width="1.2"/></svg>96% Placement Rate</li>
      <li><svg viewBox="0 0 10 10"><circle cx="5" cy="5" r="4.3" fill="none" stroke="#0b66b2" stroke-width="1.2"/><path d="M3 5.2 4.5 6.6 7.2 3.6" fill="none" stroke="#0b66b2" stroke-width="1.2"/></svg>8 Placement Coordinators</li>
      <li><svg viewBox="0 0 10 10"><circle cx="5" cy="5" r="4.3" fill="none" stroke="#0b66b2" stroke-width="1.2"/><path d="M3 5.2 4.5 6.6 7.2 3.6" fill="none" stroke="#0b66b2" stroke-width="1.2"/></svg>Relationships with 100’s of Firms</li>
    </ul>
    <div class="program-box">Westbrook Lakes University (WLU)<br><strong>Master’s in Accounting Program</strong></div>
    <div class="ranking-badge" role="img" aria-label="Ranking award badge"></div>
    <footer class="footer">
      <svg class="footer-shape" viewBox="0 0 350 50"><rect width="350" height="50" fill="#0c0c0c"/><polygon points="0,0 146,0 152,50 0,50" fill="#17a8e8"/></svg>
      <p class="org-name">Northgate Career Services</p>
      <p class="org-parent">A NON-PROFIT OF HARBOR TRUST</p>
      <ul class="contact">
        <li class="address"><svg viewBox="0 0 6 6"><path d="M3 6 C1 3.6 1 3 1 2.2 A2 2 0 0 1 5 2.2 C5 3 5 3.6 3 6 Z" fill="none" stroke="#fff" stroke-width=".7"/></svg>Riverton, Oakdale, Avon Main Branch</li>
        <li><svg viewBox="0 0 6 6"><circle cx="3" cy="3" r="2.5" fill="none" stroke="#fff" stroke-width=".6"/><path d="M.5 3h5M3 .5v5" stroke="#fff" stroke-width=".5"/></svg>www.ngcareers.org &nbsp;555 010 4400 x 210</li>
        <li><svg viewBox="0 0 6 6"><rect x=".5" y="1.2" width="5" height="3.6" fill="none" stroke="#fff" stroke-width=".6"/><path d="M.5 1.2 3 3.2 5.5 1.2" fill="none" stroke="#fff" stroke-width=".6"/></svg>admissions@ngjobs.org</li>
      </ul>
      <p class="audience">MEN &amp;<br>WOMAN</p>
    </footer>
  </article>

  <!-- Variation B -->
  <article class="flyer flyer--b">
    <div class="hero-photo" role="img" aria-label="Photo of financial charts, spreadsheets and a calculator on a desk, darkened blue"></div>
    <p class="lead">Advance your career with a</p>
    <h1 class="headline">MASTER’S OF<br>SCIENCE IN<br>ACCOUNTING</h1>
    <p class="since">Since 2005</p>
    <p class="duration">Master’s in only 15 months</p>
    <svg class="swoosh" viewBox="0 0 160 22"><path d="M2 18 C40 2 110 0 158 4 C110 4 50 10 10 22 Z" fill="#ffd200"/></svg>
    <svg class="promo-band" viewBox="0 0 350 70"><polygon points="0,5 240,5 262,69 0,69" fill="#0b66b2"/><polygon points="238,2 350,2 350,59 213,59" fill="#17a8e8"/></svg>
    <p class="promo-new">NEW!</p>
    <p class="promo-remote">REMOTE PROGRAM<br>FOR OUT OF TOWN<br>STUDENTS</p>
    <div class="promo-date"><p class="begin">BEGINNING</p><p class="date">AUGUST 17</p><p class="price">NEW LOWER PRICES</p></div>
    <h2 class="advantage-title">Northgate Job Placement Advantage</h2>
    <ul class="advantage-list">
      <li><svg viewBox="0 0 10 10"><circle cx="5" cy="5" r="4.3" fill="none" stroke="#0b66b2" stroke-width="1.2"/><path d="M3 5.2 4.5 6.6 7.2 3.6" fill="none" stroke="#0b66b2" stroke-width="1.2"/></svg>96% Placement Rate</li>
      <li><svg viewBox="0 0 10 10"><circle cx="5" cy="5" r="4.3" fill="none" stroke="#0b66b2" stroke-width="1.2"/><path d="M3 5.2 4.5 6.6 7.2 3.6" fill="none" stroke="#0b66b2" stroke-width="1.2"/></svg>8 Placement Coordinators</li>
      <li><svg viewBox="0 0 10 10"><circle cx="5" cy="5" r="4.3" fill="none" stroke="#0b66b2" stroke-width="1.2"/><path d="M3 5.2 4.5 6.6 7.2 3.6" fill="none" stroke="#0b66b2" stroke-width="1.2"/></svg>Relationships with 100’s of Firms</li>
    </ul>
    <div class="program-box">Westbrook Lakes University (WLU)<br><strong>Master’s in Accounting Program</strong></div>
    <div class="ranking-badge" role="img" aria-label="Ranking award badge"></div>
    <footer class="footer">
      <svg class="footer-shape" viewBox="0 0 350 50"><rect width="350" height="50" fill="#0c0c0c"/><polygon points="0,0 146,0 152,50 0,50" fill="#17a8e8"/></svg>
      <p class="org-name">Northgate Career Services</p>
      <p class="org-parent">A NON-PROFIT OF HARBOR TRUST</p>
      <ul class="contact">
        <li class="address"><svg viewBox="0 0 6 6"><path d="M3 6 C1 3.6 1 3 1 2.2 A2 2 0 0 1 5 2.2 C5 3 5 3.6 3 6 Z" fill="none" stroke="#fff" stroke-width=".7"/></svg>Riverton, Oakdale, Avon Main Branch</li>
        <li><svg viewBox="0 0 6 6"><circle cx="3" cy="3" r="2.5" fill="none" stroke="#fff" stroke-width=".6"/><path d="M.5 3h5M3 .5v5" stroke="#fff" stroke-width=".5"/></svg>www.ngcareers.org &nbsp;555 010 4400 x 210</li>
        <li><svg viewBox="0 0 6 6"><rect x=".5" y="1.2" width="5" height="3.6" fill="none" stroke="#fff" stroke-width=".6"/><path d="M.5 1.2 3 3.2 5.5 1.2" fill="none" stroke="#fff" stroke-width=".6"/></svg>admissions@ngjobs.org</li>
      </ul>
      <p class="audience">MEN &amp;<br>WOMAN</p>
    </footer>
  </article>

  <!-- Variation C -->
  <article class="flyer flyer--c">
    <div class="hero-photo" role="img" aria-label="Photo of accounting reports, a plant and a pie chart on a desk, darkened grey"></div>
    <p class="lead">Advance your career with a</p>
    <h1 class="headline">MASTER’S OF<br>SCIENCE IN<br>ACCOUNTING</h1>
    <p class="since">Since 2005</p>
    <p class="duration">Master’s in only 15 months</p>
    <svg class="swoosh" viewBox="0 0 160 22"><path d="M2 18 C40 2 110 0 158 4 C110 4 50 10 10 22 Z" fill="#ffd200"/></svg>
    <svg class="promo-band" viewBox="0 0 350 70"><polygon points="0,5 240,5 262,69 0,69" fill="#0b66b2"/><polygon points="238,2 350,2 350,59 213,59" fill="#17a8e8"/></svg>
    <p class="promo-new">NEW!</p>
    <p class="promo-remote">REMOTE PROGRAM<br>FOR OUT OF TOWN<br>STUDENTS</p>
    <div class="promo-date"><p class="begin">BEGINNING</p><p class="date">AUGUST 17</p><p class="price">NEW LOWER PRICES</p></div>
    <h2 class="advantage-title">Northgate Job Placement Advantage</h2>
    <ul class="advantage-list">
      <li><svg viewBox="0 0 10 10"><circle cx="5" cy="5" r="4.3" fill="none" stroke="#0b66b2" stroke-width="1.2"/><path d="M3 5.2 4.5 6.6 7.2 3.6" fill="none" stroke="#0b66b2" stroke-width="1.2"/></svg>96% Placement Rate</li>
      <li><svg viewBox="0 0 10 10"><circle cx="5" cy="5" r="4.3" fill="none" stroke="#0b66b2" stroke-width="1.2"/><path d="M3 5.2 4.5 6.6 7.2 3.6" fill="none" stroke="#0b66b2" stroke-width="1.2"/></svg>8 Placement Coordinators</li>
      <li><svg viewBox="0 0 10 10"><circle cx="5" cy="5" r="4.3" fill="none" stroke="#0b66b2" stroke-width="1.2"/><path d="M3 5.2 4.5 6.6 7.2 3.6" fill="none" stroke="#0b66b2" stroke-width="1.2"/></svg>Relationships with 100’s of Firms</li>
    </ul>
    <div class="program-box">Westbrook Lakes University (WLU)<br><strong>Master’s in Accounting Program</strong></div>
    <div class="ranking-badge" role="img" aria-label="Ranking award badge"></div>
    <footer class="footer">
      <svg class="footer-shape" viewBox="0 0 350 50"><rect width="350" height="50" fill="#0c0c0c"/><polygon points="0,0 146,0 152,50 0,50" fill="#17a8e8"/></svg>
      <p class="org-name">Northgate Career Services</p>
      <p class="org-parent">A NON-PROFIT OF HARBOR TRUST</p>
      <ul class="contact">
        <li class="address"><svg viewBox="0 0 6 6"><path d="M3 6 C1 3.6 1 3 1 2.2 A2 2 0 0 1 5 2.2 C5 3 5 3.6 3 6 Z" fill="none" stroke="#fff" stroke-width=".7"/></svg>Riverton, Oakdale, Avon Main Branch</li>
        <li><svg viewBox="0 0 6 6"><circle cx="3" cy="3" r="2.5" fill="none" stroke="#fff" stroke-width=".6"/><path d="M.5 3h5M3 .5v5" stroke="#fff" stroke-width=".5"/></svg>www.ngcareers.org &nbsp;555 010 4400 x 210</li>
        <li><svg viewBox="0 0 6 6"><rect x=".5" y="1.2" width="5" height="3.6" fill="none" stroke="#fff" stroke-width=".6"/><path d="M.5 1.2 3 3.2 5.5 1.2" fill="none" stroke="#fff" stroke-width=".6"/></svg>admissions@ngjobs.org</li>
      </ul>
      <p class="audience">MEN &amp;<br>WOMAN</p>
    </footer>
  </article>
</div>
</body>
</html>
```